talmu

We are a group of companies that we want to make a triptych. we want the general information of the work we do and the information of each company with its logo

```html
<!DOCTYPE html>
<html lang="es">
<head>
<meta charset="utf-8">
<title>Power Team KRN Talmu – Grupo de Construcción</title>
<link rel="stylesheet" href="https://fonts.googleapis.com/css2?family=Anton&family=Arimo:wght@700&family=Open+Sans:wght@400;600;700;800&display=swap">
<style>
:root{
  --kraft:#b08552;
  --teal:#0f5b7e;
  --teal-dark:#0b4a68;
  --paper:#f1f1f2;
  --gold:#f6b916;
  --gold-dark:#b87a05;
  --bullet:#f39c12;
  --bullet-hi:#ffd35a;
  --ink:#2c2c2c;
  --label:#f3efe9;
  --ribbon:#f2c56a;
}
*{box-sizing:border-box;margin:0;padding:0}
html,body{width:739px;height:1200px;overflow:hidden}
body{background:var(--kraft);font-family:"Open Sans",Arial,sans-serif;position:relative}
.sheet{position:absolute;inset:0}
.side-label{position:absolute;font-family:"Arimo",Arial,sans-serif;font-weight:700;font-size:13.5px;color:var(--label);width:120px;text-align:center}
.fold{position:absolute;width:0;border-left:1px dashed rgba(255,255,255,.55)}
.crop{position:absolute;background:#5a3e1e}
.crop.h{height:1px;width:8px}
.crop.v{width:1px;height:8px}
.panel{position:absolute;overflow:hidden}
.panel.blue{background:var(--teal);color:#fff}
.panel.light{background:var(--paper);color:var(--ink)}
.services{list-style:none}
.services li{position:relative;padding-left:11px;font-size:7.3px;line-height:9.1px;margin-bottom:3.4px}
.services li::before{content:"";position:absolute;left:0;top:1.6px;width:6.4px;height:6.4px;border-radius:50%;
  background:radial-gradient(circle at 35% 35%,var(--bullet-hi),var(--bullet) 60%,#d9820a)}
.section-title{font-weight:700;font-size:11.8px;line-height:14px;text-transform:uppercase;padding:8px 10px 7px 16px}
.section-title.on-blue{background:var(--teal);color:#fff}
.section-title.on-light{background:var(--paper);color:var(--teal)}
/* side 5 */
.services-overview{left:35px;top:46px;width:227px;height:524px;padding:22px 8px 0 22px}
/* side 6 */
.members{left:262px;top:46px;width:219px;height:524px}
.member{position:absolute;left:0;right:0;text-align:center;font-weight:700;font-size:15px;color:#3b3b3b;display:flex;align-items:center;justify-content:center;gap:7px}
.member .dot{width:9px;height:9px;background:var(--teal);display:inline-block}
/* side 1 */
.cover{left:481px;top:46px;width:228px;height:524px;background:linear-gradient(180deg,#12638a,var(--teal) 60%,var(--teal-dark))}
.cover-title{position:absolute;top:30px;left:0;right:0;text-align:center;font-family:"Anton",Impact,sans-serif;font-size:40px;line-height:40px;color:var(--gold);
  text-shadow:2px 2px 0 var(--gold-dark),3px 4px 4px rgba(0,0,0,.45);letter-spacing:.5px}
.cover-sub{position:absolute;top:176px;left:0;right:0;text-align:center;font-size:16px;color:#fff}
.badge{position:absolute;left:155px;top:216px;width:78px;height:78px;margin-left:-39px;border-radius:50%;background:#fff;border:4px solid #d5d9dc;
  display:flex;align-items:center;justify-content:center;text-align:center;font-weight:700;font-size:11.5px;line-height:14px;color:#444}
.ribbon{position:absolute;left:0;top:270px;width:186px;height:46px}
.team-photo{position:absolute;left:5px;top:282px;width:212px;height:200px;border-radius:45% 45% 35% 35%;
  background:radial-gradient(ellipse at 50% 40%,#e8dcd2,#9aa3ad 55%,rgba(15,91,126,0) 75%)}
.cover-web{position:absolute;top:487px;left:0;right:0;text-align:center;font-weight:700;font-size:14px;letter-spacing:1.6px;color:#fff}
/* bottom row */
.private-projects{left:35px;top:606px;width:227px;height:522px;padding-top:22px}
.private-build{left:262px;top:606px;width:219px;height:522px;padding-top:24px}
.business-build{left:481px;top:606px;width:228px;height:522px;padding-top:24px}
.private-projects .services{padding:10px 8px 0 29px}
.private-projects .section-title{margin-left:0}
.private-projects .services.first{margin-bottom:14px}
.private-build .services{padding:0 8px 0 16px}
.private-build .services.lead{margin-bottom:18px}
.private-build .section-title{margin-bottom:8px}
.business-build .services{padding:0 8px 0 12px}
.business-build .services.lead{margin-bottom:9px}
.business-build .section-title{margin-bottom:8px}
</style>
</head>
<body>
<div class="sheet">

  <div class="side-label" style="left:88px;top:23px">Side 5</div>
  <div class="side-label" style="left:309px;top:23px">Side 6</div>
  <div class="side-label" style="left:526px;top:23px">Side 1</div>
  <div class="side-label" style="left:100px;top:1141px">Side 2</div>
  <div class="side-label" style="left:325px;top:1141px">Side 3</div>
  <div class="side-label" style="left:543px;top:1141px">Side 4</div>

  <div class="fold" style="left:262px;top:30px;height:14px"></div>
  <div class="fold" style="left:481px;top:30px;height:14px"></div>
  <div class="fold" style="left:262px;top:592px;height:12px"></div>
  <div class="fold" style="left:481px;top:592px;height:12px"></div>
  <div class="fold" style="left:262px;top:1130px;height:10px"></div>
  <div class="fold" style="left:481px;top:1130px;height:10px"></div>

  <div class="crop v" style="left:35px;top:36px"></div>
  <div class="crop v" style="left:709px;top:36px"></div>
  <div class="crop h" style="left:25px;top:46px"></div>
  <div class="crop h" style="left:711px;top:46px"></div>
  <div class="crop h" style="left:25px;top:570px"></div>
  <div class="crop h" style="left:711px;top:570px"></div>
  <div class="crop v" style="left:35px;top:596px"></div>
  <div class="crop v" style="left:709px;top:596px"></div>
  <div class="crop h" style="left:25px;top:606px"></div>
  <div class="crop h" style="left:711px;top:606px"></div>
  <div class="crop h" style="left:25px;top:1128px"></div>
  <div class="crop h" style="left:711px;top:1128px"></div>

  <!-- Side 5 -->
  <section class="panel blue services-overview">
    <ul class="services">
      <li>Asesoramiento sobre las mejores soluciones de eficiencia energética en el equipamiento de locales comerciales, hoteles y toda clase de edificios públicos que precisen de una mejora en su consumo de energía</li>
      <li>Albañilería tradicional de ladrillo y tabiquería en seco tipo Placor, ya sea estándar o con re-querimientos acústicos y/o de protección al fuego especiales</li>
      <li>Pintura de viviendas y aparcamientos, aplicando en cada caso el producto más adecuado a las necesidades y las exigencias de su uso</li>
      <li>Falsos techos registrables y fijos</li>
      <li>Impermeabilización y aislamiento térmico, acústico y estanco</li>
      <li>Impermeabilización de elementos especiales de exterior, en especial paredes medianeras</li>
      <li>Instalación y mantenimiento de climatización. Además de los métodos tradicionales, como la climatización por aire, por radiadores o convectores, somo expertos en aerotermia, geotermia y energía solar, así como el tratamiento del aire en entornos que requieran de una calidad es-pecial en este aspecto</li>
      <li>Alicatados en cocinas y baños</li>
      <li>Chapados y revestimientos de paredes y fachadas</li>
      <li>Pavimentos de madera, cerámica y piedra, así como pavimentos técnicos</li>
      <li>Carpintería de madera en interiores</li>
      <li>Recuperación de elementos interiores de madera</li>
      <li>Carpintería de aluminio</li>
      <li>Instalación y mantenimiento de electricidad y domótica</li>
      <li>Instalación y mantenimiento de sistemas de alumbrado, tanto en interiores como en exteriores</li>
      <li>Instalación y mantenimiento de alumbrado de emergencia</li>
      <li>Instalación y mantenimiento de instalación de fontanería y saneamiento</li>
      <li>Instalación de ascensores</li>
      <li>Instalación y mantenimiento de instalaciones de protección especializada contra incendios mediante agua, gases inertes, sistemas especiales para cocinas industriales, columna seca, de-pósitos de agua, señalización, puertas cortafuegos, telas ignífugas o sellado de pasos de insta-laciones</li>
    </ul>
  </section>

  <!-- Side 6 -->
  <section class="panel light members" aria-label="Empresas del grupo">
    <div class="member" style="top:44px">nordcuina studio</div>
    <div class="member" style="top:128px"><span class="dot"></span>Fustes Orla S.L.</div>
    <div class="member" style="top:204px">mirel.sl</div>
    <div class="member" style="top:268px">vent interiorisme</div>
    <div class="member" style="top:332px"><span class="dot"></span>arca facility</div>
    <div class="member" style="top:400px">Serra Arquitectes</div>
    <div class="member" style="top:460px"><span class="dot"></span>lumvid</div>
  </section>

  <!-- Side 1 -->
  <section class="panel cover">
    <h1 class="cover-title">POWER<br>TEAM KRN<br>TALMU</h1>
    <p class="cover-sub">Grupo de Construcción</p>
    <div class="team-photo" role="img" aria-label="Fotografía de un equipo de profesionales sonrientes con el pulgar hacia arriba"></div>
    <svg class="ribbon" viewBox="0 0 186 46" role="img" aria-label="Cinta decorativa dorada">
      <rect x="0" y="8" width="186" height="30" fill="var(--ribbon)"/>
    </svg>
    <div class="badge">Somos un<br>grupo de<br>empresas</div>
    <p class="cover-web">www.talmugrup.com</p>
  </section>

  <!-- Side 2 -->
  <section class="panel light private-projects">
    <h2 class="section-title on-blue">Diseño y gestión de proyectos y obras para particulares</h2>
    <ul class="services first">
      <li>Proyecto de obra nueva</li>
      <li>Proyecto de reforma y rehabilitación</li>
      <li>Proyecto de interiorismo y decoración</li>
      <li>Proyecto de cambio de uso de locales comerciales y oficinas a vivienda</li>
      <li>Proyecto de legalización de viviendas y otras construcciones</li>
      <li>Tramitación de licencia de obras ante ayuntamientos y administraciones equivalentes</li>
      <li>Dirección de obra</li>
      <li>Comercialización y valoración de inmuebles, tanto para clientes nacionales como extranjeros que busquen propiedades en España, con especial énfasis en viviendas de alto standing en zonas costeras</li>
    </ul>
    <h2 class="section-title on-blue">Diseño y gestión de proyectos y obras para empresas y negocios</h2>
    <ul class="services">
      <li>Proyecto de obra nueva</li>
      <li>Proyecto de reforma y rehabilitación</li>
      <li>Proyecto de interiorismo y decoración de hoteles, locales comerciales, oficinas y edificios públicos en general</li>
      <li>Estudio de viabilidad de promociones inmobiliarias</li>
      <li>Búsqueda de terrenos y edificios para promociones inmobiliarias, gestión patrimonial y grupos inversores</li>
      <li>Búsqueda de compradores e inversores para los inmuebles de nuestros clientes</li>
      <li>Proyecto de urbanización de terrenos ubicados en zonas afectadas por planes parciales</li>
      <li>Proyecto de cambio de uso de edificios construidos, ya sean hoteles, viviendas, locales, ofici-nas, al uso que el cliente solicite, previa consulta con las administraciones competentes para validar la viabilidad del proceso</li>
      <li>Tramitación de licencia de obras ante</li>
    </ul>
  </section>

  <!-- Side 3 -->
  <section class="panel blue private-build">
    <ul class="services lead">
      <li>ayuntamientos y administraciones equivalentes</li>
      <li>Dirección de obra</li>
      <li>Comercialización y valoración de inmuebles, tanto para clientes nacionales como extranjeros que busquen propiedades en España</li>
    </ul>
    <h2 class="section-title on-light">Construcción y obra para particulares</h2>
    <ul class="services">
      <li>Derribo de construcciones</li>
      <li>Excavación y movimiento de tierras</li>
      <li>Cimentaciones de viviendas</li>
      <li>Estructuras de hormigón, acero y madera para viviendas nuevas</li>
      <li>Refuerzo y reparación de estructuras de hormigón, acero y madera para rehabilitación y/o re-forma de viviendas</li>
      <li>Diseño y construcción de mobiliario a medida</li>
      <li>Diseño y construcción de cocinas a medida de la marca Oliva</li>
      <li>Reforma y rehabilitación de cocinas y baños</li>
      <li>Albañilería tradicional de ladrillo y tabiquería en seco tipo Placor</li>
      <li>Pintura de viviendas y aparcamientos en edificios de viviendas</li>
      <li>Pintura de protección de elementos especiales</li>
      <li>Falsos techos registrables y fijos</li>
      <li>Construcción y reforma de cubiertas, planas o inclinadas, transitables o técnicas, en viviendas y edificios de viviendas</li>
      <li>Impermeabilización y aislamiento térmico, acústico y estanco en viviendas nuevas y a rehabi-litar o reformar</li>
      <li>Impermeabilización de medianeras mediante tabiques pluviales de diferentes tipos</li>
      <li>Instalación y mantenimiento de calefacción por aire y radiador</li>
      <li>Instalación y mantenimiento de climatización por aire</li>
      <li>Alicatados en cocinas y baños</li>
      <li>Chapados y revestimientos en viviendas y zonas comunes de edificios de viviendas</li>
      <li>Pavimentos de madera, cerámica y piedra en viviendas y zonas comunes de viviendas</li>
    </ul>
  </section>

  <!-- Side 4 -->
  <section class="panel light business-build">
    <ul class="services lead">
      <li>Carpintería de madera en interiores de viviendas</li>
      <li>Carpintería de aluminio en viviendas y edificios de viviendas</li>
      <li>Instalación y mantenimiento de electricidad y domótica</li>
      <li>Instalación y mantenimiento de sistemas de alumbrado, tanto en interiores como en exteriores</li>
      <li>Instalación y mantenimiento de alumbrado de emergencia en zonas comunes de edificios de viviendas</li>
      <li>Instalación y mantenimiento de instalación de fontanería y saneamiento</li>
      <li>Instalación de ascensores especiales para viviendas</li>
      <li>Instalación y mantenimiento de instalaciones de protección contra incendios en aparcamientos de viviendas unifamiliares, aparcamientos de edificios de viviendas y zonas comunes de edificios de viviendas</li>
    </ul>
    <h2 class="section-title on-blue">Construcción y obra para empresas y negocios</h2>
    <ul class="services">
      <li>Derribo de construcciones</li>
      <li>Excavación y movimiento de tierras</li>
      <li>Cimentaciones de edificios</li>
      <li>Estructuras de hormigón, acero y madera</li>
      <li>Refuerzo, reparación y modificacióndde estructuras de hormigón, acero y madera para rehabi-litación y/o reforma de edificios</li>
      <li>Diseño y construcción de mobiliario a medida para locales comerciales, oficinas, hoteles y edificios destinados al sector terciario en general</li>
      <li>Diseño y construcción de cocinas a medida de la marca Oliva</li>
      <li>Diseño, construcción y mantenimiento de cocinas industriales a medida para hoteles, restau-rantes, cafeterías, escuelas, hospitales y cualquier establecimiento público que necesite este tipo de servicio, completamente equipada con la maquinaria más adecuada a sus requerimien-tos</li>
      <li>Reforma y rehabilitación de cocinas y baños en todo tipo de edificios públicos</li>
      <li>Pintura de protección de elementos especiales</li>
      <li>Construcción y reforma de cubiertas, tanto transitables como técnicas</li>
    </ul>
  </section>

</div>
</body>
</html>
```